Brightmoor Partners Branding Revamp

We are a consulting company, looking for a way to display and promote our brand. We have 2 sides to the business- Brightmoor (financial) and Partners (cyber security). The financial side products relate to business necessities: card processing, website design/hosting/maintenance, VoIP phone systems. The cyber security side promotes a bundled package of 4 solutions: network vulnerability scan, dark web scan, anti-ransomeware/malware software, and image-level backups. We want people to understand that partnering with Brightmoor Partners gives them “Elevated Peace of Mind” (tagline). Current badge and logos uploaded.

Target Market(s)

Small businesses

Contact Information for Business Card

Lena Marwick, Vice President, lena@brightmoorpartners.example, 555-806-1937, www.brightmoorpartners.example

Requirements
Nice to have
• I do prefer the darker background for front and back

```html
<!DOCTYPE html>
<html lang="en">
<head>
<meta charset="utf-8">
<title>Brightmoor Partners — Business Card</title>
<link href="https://fonts.googleapis.com/css2?family=Arimo:wght@400;700&display=swap" rel="stylesheet">
<style>
  :root {
    --page: #f2f2f2;
    --charcoal: #333235;
    --signal-red: #e93236;
    --white: #ffffff;
    --soft-white: #f4f4f4;
  }
  * { box-sizing: border-box; margin: 0; padding: 0; }
  html, body {
    width: 1200px;
    height: 996px;
    overflow: hidden;
    background: var(--page);
    font-family: "Arimo", Arial, sans-serif;
  }
  .card-sheet {
    position: relative;
    width: 1200px;
    height: 996px;
  }
  .card {
    position: absolute;
    top: 340px;
    width: 555px;
    height: 316px;
    background: var(--charcoal);
    overflow: hidden;
    box-shadow: 0 2px 6px rgba(0,0,0,0.12);
  }
  .card--front { left: 30px; }
  .card--back { left: 615px; }

  /* brand lockup */
  .brand-lockup {
    display: flex;
    flex-direction: column;
    align-items: center;
    gap: 18px;
  }
  .brand-mark {
    width: 46px;
    height: 46px;
    background: var(--signal-red);
  }
  .brand-name {
    color: var(--white);
    font-weight: 400;
    font-size: 19px;
    letter-spacing: 4px;
    text-transform: uppercase;
    white-space: nowrap;
  }

  /* front */
  .front-field {
    position: absolute;
    left: 0; top: 0;
    width: 390px;
    height: 100%;
    display: flex;
    align-items: center;
    justify-content: center;
  }
  .front-band {
    position: absolute;
    right: 0; top: 0;
    width: 165px;
    height: 100%;
    background: var(--signal-red);
    display: flex;
    align-items: center;
    justify-content: center;
  }
  .front-url {
    writing-mode: vertical-rl;
    color: var(--white);
    font-size: 17px;
    letter-spacing: 0.3px;
  }

  /* back */
  .back-field {
    position: absolute;
    left: 0; top: 0;
    width: 100%;
    height: 200px;
    display: flex;
    align-items: center;
    justify-content: center;
  }
  .back-band {
    position: absolute;
    left: 0; bottom: 0;
    width: 100%;
    height: 116px;
    background: var(--signal-red);
  }
  .person {
    position: absolute;
    left: 32px;
    top: 36px;
    color: var(--white);
  }
  .person-name {
    font-weight: 700;
    font-size: 20px;
  }
  .person-title {
    font-size: 16px;
    margin-top: 2px;
    color: var(--soft-white);
  }
  .contact-list {
    position: absolute;
    left: 293px;
    top: 20px;
    list-style: none;
    color: var(--white);
    font-size: 14.5px;
  }
  .contact-item {
    display: flex;
    align-items: center;
    gap: 8px;
    height: 26px;
  }
  .contact-icon {
    width: 14px;
    height: 14px;
    flex: none;
  }
</style>
</head>
<body>
<main class="card-sheet">
  <section class="card card--front" aria-label="Card front">
    <div class="front-field">
      <div class="brand-lockup">
        <span class="brand-mark" aria-hidden="true"></span>
        <span class="brand-name">Brightmoor Partners</span>
      </div>
    </div>
    <div class="front-band">
      <span class="front-url">www.brightmoorpartners.example</span>
    </div>
  </section>

  <section class="card card--back" aria-label="Card back">
    <div class="back-field">
      <div class="brand-lockup">
        <span class="brand-mark" aria-hidden="true"></span>
        <span class="brand-name">Brightmoor Partners</span>
      </div>
    </div>
    <div class="back-band">
      <div class="person">
        <p class="person-name">Lena Marwick</p>
        <p class="person-title">Vice President</p>
      </div>
      <ul class="contact-list">
        <li class="contact-item">
          <svg class="contact-icon" viewBox="0 0 14 14" aria-hidden="true">
            <rect x="0.5" y="2.5" width="13" height="9" fill="#fff"/>
            <path d="M0.5 2.5 L7 8 L13.5 2.5" fill="none" stroke="#e93236" stroke-width="1.2"/>
          </svg>
          <span>lena@brightmoorpartners.example</span>
        </li>
        <li class="contact-item">
          <svg class="contact-icon" viewBox="0 0 14 14" aria-hidden="true">
            <rect x="3.5" y="0.8" width="7" height="12.4" rx="1.2" fill="none" stroke="#fff" stroke-width="1.3"/>
            <line x1="6" y1="11" x2="8" y2="11" stroke="#fff" stroke-width="1.2"/>
          </svg>
          <span>555-806-1937</span>
        </li>
        <li class="contact-item">
          <svg class="contact-icon" viewBox="0 0 14 14" aria-hidden="true">
            <g fill="none" stroke="#fff" stroke-width="1.1">
              <circle cx="7" cy="7" r="6"/>
              <ellipse cx="7" cy="7" rx="2.6" ry="6"/>
              <line x1="1" y1="7" x2="13" y2="7"/>
              <path d="M2 4 H12 M2 10 H12"/>
            </g>
          </svg>
          <span>www.brightmoorpartners.example</span>
        </li>
      </ul>
    </div>
  </section>
</main>
</body>
</html>
```